EG 1 page flyer

I need a flyer design for a financial risk advisory business. I like the layout of the example on your site, for Corbin Delph (attached). Our business needs to show strength, safety, knowledge and security. We provide financial advice.

I have uploaded the front page of our larger brochure. I would like the man with the umbrella with the caption and the logo / brand on the front page, but with portrait orientation, instead of landscape.

For the second page (the back), I have got some ideas of the kinds of things I would want written on the attached Power Point. But it needs to be arranged better, with perhaps the Elsie's Gate Logo on there as well, to break up all the writing. Attached is an example of how it might look, but I want different formatting and layout ideas, that look better, more professional etc.

The page 1 comment what is elsies gate? predicting ......... would look better all the way along the bottom of the page, but i couldn't get the formatting right.

Financial

```html
<!DOCTYPE html>
<html lang="en">
<head>
<meta charset="utf-8">
<title>Elsie's Gate – Financial Risk Advisory</title>
<link href="https://fonts.googleapis.com/css2?family=Ubuntu:ital,wght@0,300;0,400;0,500;0,700;1,300;1,400;1,700&display=swap" rel="stylesheet">
<style>
  :root {
    --navy: #232a5c;
    --band-deep: #1e2656;
    --band-mid: #203a72;
    --band-light: #1570aa;
    --sky: #1ea6e6;
    --headline: #2db6f0;
    --white: #ffffff;
    --ink: #1d1d1d;
    --grey-dark: #a4a4a4;
    --grey-light: #d9d9d9;
  }
  html, body {
    margin: 0;
    padding: 0;
    width: 887px;
    height: 1200px;
    overflow: hidden;
    background: var(--white);
  }
  .flyer {
    position: relative;
    width: 887px;
    height: 1200px;
    overflow: hidden;
    font-family: "Ubuntu", sans-serif;
    background: var(--white);
  }

  /* Header */
  .brand {
    position: absolute;
    left: 97px;
    top: 70px;
  }
  .brand-mark {
    position: absolute;
    left: 250px;
    top: 2px;
    width: 78px;
    height: 78px;
    border-radius: 50%;
    background: var(--navy);
  }
  .brand-name {
    position: absolute;
    left: 0;
    top: 76px;
    margin: 0;
    font-size: 58px;
    font-weight: 500;
    line-height: 1;
    letter-spacing: -1px;
    color: var(--navy);
    white-space: nowrap;
  }
  .brand-tagline {
    position: absolute;
    left: 1px;
    top: 138px;
    margin: 0;
    font-size: 17px;
    font-weight: 400;
    color: var(--sky);
    white-space: nowrap;
    word-spacing: 2px;
  }
  .brand-tagline span + span { margin-left: 12px; }

  .slogan {
    position: absolute;
    left: 531px;
    top: 120px;
    margin: 0;
    font-size: 23px;
    font-weight: 700;
    line-height: 28px;
    color: var(--sky);
  }

  /* Hero band */
  .hero {
    position: absolute;
    left: 0;
    top: 343px;
    width: 887px;
    height: 600px;
    background: linear-gradient(100deg, var(--band-deep) 0%, var(--band-deep) 35%, var(--band-mid) 62%, var(--band-light) 100%);
  }
  .hero-photo {
    position: absolute;
    left: 470px;
    top: 290px;
    width: 330px;
    height: 653px;
    background: radial-gradient(ellipse at 55% 35%, rgba(40,44,52,0.85) 0%, rgba(30,34,44,0.65) 45%, rgba(25,40,70,0.0) 75%);
  }
  .hero-title {
    position: absolute;
    left: 97px;
    top: 488px;
    margin: 0;
    font-size: 62px;
    font-weight: 700;
    font-style: italic;
    line-height: 70px;
    letter-spacing: -2px;
    color: var(--headline);
    text-shadow: 3px 3px 4px rgba(0, 0, 0, 0.55);
  }
  .services {
    position: absolute;
    left: 108px;
    top: 684px;
    margin: 0;
    padding: 0;
    list-style: none;
  }
  .service {
    display: flex;
    align-items: center;
    height: 48px;
    margin-bottom: 32px;
    font-size: 26px;
    font-weight: 300;
    font-style: italic;
    color: var(--white);
    text-shadow: 1px 1px 2px rgba(0,0,0,0.5);
  }
  .service svg {
    width: 66px;
    height: 48px;
    margin-right: 12px;
    flex: none;
  }

  /* Footer band */
  .footer {
    position: absolute;
    left: 0;
    top: 955px;
    width: 887px;
    height: 245px;
    background: linear-gradient(110deg, var(--grey-dark) 0%, #bdbdbd 45%, var(--grey-light) 100%);
  }
  .footer-question {
    position: absolute;
    left: 381px;
    top: 50px;
    margin: 0;
    font-size: 38px;
    font-weight: 300;
    color: var(--ink);
    white-space: nowrap;
  }
  .footer-quote {
    position: absolute;
    left: 382px;
    top: 110px;
    margin: 0;
    font-size: 21px;
    font-weight: 700;
    line-height: 26px;
    color: var(--ink);
  }
</style>
</head>
<body>
<div class="flyer">

  <header class="brand">
    <span class="brand-mark" aria-hidden="true"></span>
    <h1 class="brand-name">Elsie’s Gate</h1>
    <p class="brand-tagline"><span>Our experience</span><span>Your edge</span></p>
  </header>

  <p class="slogan">Whatever the<br>Financial Forecast...<br>It pays to be prepared!</p>

  <section class="hero">
    <h2 class="hero-title" style="top:145px">Financial<br>Risk Advisory</h2>
    <ul class="services" style="top:341px">
      <li class="service">
        <svg viewBox="0 0 66 48" aria-hidden="true">
          <rect x="2" y="20" width="50" height="22" rx="2" fill="none" stroke="#fff" stroke-width="2.5"/>
          <rect x="7" y="14" width="50" height="22" rx="2" fill="var(--band-deep)" stroke="#fff" stroke-width="2.5"/>
          <rect x="12" y="8" width="50" height="22" rx="2" fill="#fff"/>
          <circle cx="37" cy="19" r="8" fill="var(--band-deep)"/>
          <text x="37" y="24" text-anchor="middle" font-family="Ubuntu, sans-serif" font-weight="700" font-size="13" fill="#fff">$</text>
        </svg>
        Debt &amp; Funding
      </li>
      <li class="service">
        <svg viewBox="0 0 66 48" aria-hidden="true">
          <path d="M26 6 L48 44 L4 44 Z" fill="#fff" stroke="#fff" stroke-width="3" stroke-linejoin="round"/>
          <rect x="24" y="20" width="4" height="13" rx="2" fill="var(--band-deep)"/>
          <circle cx="26" cy="38" r="2.4" fill="var(--band-deep)"/>
          <circle cx="48" cy="12" r="11" fill="#fff"/>
          <path d="M42 12 L46.5 16.5 L54 8" fill="none" stroke="var(--band-deep)" stroke-width="3" stroke-linecap="round" stroke-linejoin="round"/>
        </svg>
        Market Risk
      </li>
      <li class="service">
        <svg viewBox="0 0 66 48" aria-hidden="true">
          <g stroke="#fff" stroke-width="2.5" fill="none" stroke-linecap="round">
            <circle cx="16" cy="28" r="7"/>
            <path d="M13 37 h6 M14 40 h4"/>
            <path d="M16 15 v-3 M5 28 h-3 M30 28 h-3 M8 20 l-2 -2 M24 20 l2 -2 M8 36 l-2 2"/>
            <circle cx="44" cy="8" r="5"/>
            <path d="M36 46 V20 h16 V46 M44 30 V46"/>
          </g>
        </svg>
        Active Engagement
      </li>
    </ul>
  </section>

  <div class="hero-photo" role="img" aria-label="Photograph of a man in a dark suit and bowler hat, seated and holding a black umbrella above his head"></div>

  <footer class="footer">
    <h2 class="footer-question">What is Elsie’s Gate?</h2>
    <p class="footer-quote">Predicting rain doesn’t count;<br>building arks does”</p>
  </footer>

</div>
</body>
</html>
```